Geschäftspapiere für Rechtsanwaltskanzlei
Zielgruppe
Rechtsanwaltskanzlei
Aufgabenstellung
Bitte inklusive Logo (sollte Recht, Digital/Apps, Medizin illustrieren) - habe das Preisgeld vor diesem Hintergrund erhöht.
Die Kanzlei arbeitet an der Schnittstelle von (Medizin-)Recht und Digital. Von daher wären wären Symbole/Gestaltung aus Bereich Medizin, Recht und Digital (z.B. Apps etc.) passend.
Das Briefpapier soll alle wichtigen Infos enthalten, aber dabei sehr klar gehalten werden und nicht überladen sein. Mir ist ein schlichtes und ansprechendes Design wichtig. Es soll nicht verspielt sein.
Info auf Briefpapier:
Kanzlei für Medizinrecht
Rechtsanwalt Dr. Tilman Brecke - Fachanwalt für Medizinrecht
Bitte Platzhalter/Freitextfelder für die anderen anderen Angaben, wie:
- Adresse
- Telefon-Nr.
- Homepage
- E-Mail
- Bankdaten.

```html
<!DOCTYPE html>
<html lang="de">
<head>
<meta charset="utf-8">
<title>Kanzlei Brecke – Briefpapier</title>
<link rel="stylesheet" href="https://fonts.googleapis.com/css2?family=Open+Sans:wght@400;600&family=Arimo:wght@400&display=swap">
<style>
  :root {
    --lime: #c2d82e;
    --ink: #575757;
    --ink-soft: #6a6a6a;
    --rule: #b9b9b9;
    --paper: #ffffff;
    --backdrop: #e5e6e5;
  }
  html, body {
    margin: 0;
    width: 1151px;
    height: 1200px;
    overflow: hidden;
    background: var(--backdrop);
  }
  .sheet {
    position: absolute;
    left: 165px;
    top: 20px;
    width: 821px;
    height: 1160px;
    background: var(--paper);
    box-shadow: 0 4px 18px rgba(0,0,0,.18);
    font-family: "Open Sans", sans-serif;
    color: var(--ink);
    overflow: hidden;
  }
  .band { position: absolute; }
  .band--top { left: 0; top: 0; }
  .band--bottom { right: 0; bottom: 0; }

  .brand {
    position: absolute;
    right: 58px;
    top: 52px;
    text-align: right;
  }
  .brand__name {
    display: flex;
    align-items: center;
    justify-content: flex-end;
    gap: 9px;
    margin: 0;
    font-weight: 600;
    font-size: 24px;
    line-height: 30px;
    color: var(--ink);
  }
  .brand__mark {
    width: 12px;
    height: 12px;
    border-radius: 50%;
    background: var(--lime);
  }
  .brand__tagline {
    margin: 4px 0 0;
    font-family: "Open Sans", sans-serif;
    font-size: 12.5px;
    color: var(--ink-soft);
  }

  .contact {
    position: absolute;
    left: 564px;
    top: 149px;
    height: 122px;
    padding-left: 12px;
    border-left: 1px solid var(--ink-soft);
    font-size: 10.6px;
    line-height: 15.3px;
    font-style: normal;
    color: var(--ink-soft);
  }
  .contact p { margin: 0; }
  .contact__channels { margin: 4px 0 0; padding: 0; list-style: none; }
  .contact__channels li { display: flex; align-items: center; gap: 8px; }
  .contact__channels svg { width: 10px; height: 10px; flex: none; }

  .sender-line {
    position: absolute;
    left: 99px;
    top: 204px;
    font-size: 7.6px;
    color: var(--ink-soft);
    border-bottom: 1px solid var(--rule);
    padding-bottom: 1px;
    white-space: nowrap;
  }
  .sender-line .sep { color: var(--lime); margin: 0 2px; }

  .fold-mark {
    position: absolute;
    left: 0;
    width: 25px;
    height: 1px;
    background: var(--rule);
  }

  .letter {
    position: absolute;
    left: 104px;
    top: 404px;
    width: 664px;
    font-family: "Arimo", sans-serif;
    font-size: 13.4px;
    line-height: 15.5px;
    letter-spacing: -0.25px;
    color: var(--ink);
  }
  .letter p { margin: 0 0 15.5px; text-align: justify; }
  .letter .salutation { margin-bottom: 15px; }

  .signature {
    position: absolute;
    left: 104px;
    top: 771px;
    width: 260px;
    height: 45px;
    background: linear-gradient(90deg, #ededed, #f6f6f6);
  }

  .footer {
    position: absolute;
    top: 1083px;
    left: 380px;
    display: flex;
    font-size: 10.6px;
    line-height: 15.5px;
    color: var(--ink-soft);
  }
  .footer p { margin: 0; white-space: nowrap; }
  .footer__bank { padding-right: 16px; border-right: 1px solid var(--ink-soft); }
  .footer__tax { padding-left: 18px; }
</style>
</head>
<body>
  <main class="sheet">
    <svg class="band band--top" width="463" height="19" viewBox="0 0 463 19" aria-hidden="true">
      <path d="M0 0H463L460 13Q458 19 451 19H0Z" fill="var(--lime)"/>
    </svg>

    <header class="brand">
      <h1 class="brand__name"><span class="brand__mark"></span>Kanzlei Brecke</h1>
      <p class="brand__tagline">Medizinrecht · Digitale Gesundheit · Medizinprodukte</p>
    </header>

    <address class="contact">
      <p>Rechtsanwalt Dr. Tilman Brecke</p>
      <p>Fachanwalt für Medizinrecht</p>
      <p>Muster Weg 32</p>
      <p>10400 Muster Stadt</p>
      <ul class="contact__channels">
        <li><svg viewBox="0 0 10 10"><path d="M2 1l2 2-1 1.3q1 2 2.7 2.7L7 6l2 2-1.4 1.4Q3.8 9 .6 2.4Z" fill="var(--lime)"/></svg>+49 (0) 6100 4080 - 200</li>
        <li><svg viewBox="0 0 10 10"><rect x="2.5" y="1" width="5" height="3" fill="var(--lime)"/><rect x="1" y="4" width="8" height="4" rx="1" fill="var(--lime)"/><rect x="3" y="7" width="4" height="2.5" fill="var(--lime)"/></svg>+49 (0) 6100 4080 - 209</li>
        <li><svg viewBox="0 0 10 10"><rect x="0.5" y="2" width="9" height="6.5" fill="var(--lime)"/><path d="M.5 2.5L5 6l4.5-3.5" stroke="#fff" stroke-width="1" fill="none"/></svg>info@rechtsanwalttilmanbrecke.de</li>
        <li><svg viewBox="0 0 10 10"><circle cx="5" cy="5" r="4.5" fill="var(--lime)"/><path d="M3 3.5q1.5-1 2 .5t2 1M4 7.5q1-1.5 2.5-.5" stroke="#fff" stroke-width=".9" fill="none"/></svg>www.rechtsanwalttilmanbrecke.de</li>
      </ul>
    </address>

    <div class="sender-line">Rechtsanwalt Dr. Tilman Brecke<span class="sep">|</span>Muster Weg 32<span class="sep">|</span>10400 Muster Stadt</div>

    <span class="fold-mark" style="top:411px"></span>
    <span class="fold-mark" style="top:579px"></span>
    <span class="fold-mark" style="top:820px"></span>

    <article class="letter">
      <p class="salutation">Herr Becker</p>
      <p>Lorem ipsum dolor sit amet, consectetur adipiscing elit. Proin tincidunt, lectus id malesuada cursus, lorem augue egestas magna, ut mattis orci ante ut arcu. Sed mauris tellus, fermentum quis ligula nec, posuere pulvinar eros. Nam at mi quis velit pellentesque finibus. Donec lacus velit, faucibus mollis dolor nec, finibus pellentesque orci. Duis sed dictum elit, ut posuere arcu. Phasellus ac dolor et ante consequat rutrum nec nec tortor. Donec consequat, nibh sit amet pulvinar faucibus, turpis magna venenatis diam, vel pretium.</p>
      <p>Sed pretium ac enim eu viverra. Aliquam ac est eget magna convallis convallis. Aenean augue purus, finibus eget turpis quis, finibus dignissim nibh. Phasellus viverra lobortis dignissim. Duis varius turpis in sapien accumsan facilisis. Sed vehicula gravida diam a interdum. Nullam convallis ligula id erat egestas consequat. Integer consectetur ex vel aliquet iaculis. Vestibulum molestie sodales mauris, at tincidunt.</p>
      <p>Mauris facilisis, lectus at accumsan tincidunt, dui magna imperdiet sem, quis tempor est lectus eu ipsum. Praesent in fermentum nisl. Maecenas at lorem at odio interdum iaculis. Pellentesque cursus nulla nunc, ut suscipit nulla maximus et. Donec maximus rhoncus metus, vel laoreet nisi pretium sit amet. Donec posuere enim lectus, vitae aliquam augue tincidunt dignissim. Morbi vitae congue velit, quis elementum.</p>
      <p>Curabitur augue tortor, sagittis non metus euismod, tincidunt lacinia nibh. Praesent maximus congue est quis sodales. Nulla pharetra lobortis fringilla. Fusce sagittis orci tortor, nec laoreet mauris mattis et. Aenean eget erat sed ipsum rutrum tristique. Maecenas ut nunc in orci tincidunt lacinia eu vitae ligula. Donec aliquet ligula vitae nisi aliquet volutpat. Nullam volutpat non orci id feugiat. Etiam erat neque, condimentum sit amet quam et, tincidunt cursus odio.</p>
    </article>

    <div class="signature" role="img" aria-label="Handschriftliche Unterschrift von Dr. Tilman Brecke"></div>

    <footer class="footer">
      <div class="footer__bank">
        <p>Bank: Auenbank Musterstadt eG</p>
        <p>BIC: AUENDEFF000</p>
        <p>IBAN: DE41 7750 0012 0480 0000 19</p>
      </div>
      <div class="footer__tax">
        <p>SteurID: DE519604000</p>
        <p>Umsatzsteuer ID: 62 000 731 000</p>
      </div>
    </footer>

    <svg class="band band--bottom" width="461" height="20" viewBox="0 0 461 20" aria-hidden="true">
      <path d="M461 0V20H0L3 7Q5 0 12 0Z" fill="var(--lime)"/>
    </svg>
  </main>
</body>
</html>
```